Security Services Business Card

Looking for a clean modern style business card design for a residential and commercial security solutions provider. We install and service the following
security alarm, access control, video surveillance and fire alarm. Attached are the front and back of our current business cards in PSD file format.

Target Market(s)

Security alarm clients in the commercial and residential markets

Industry/Entity Type

Security Service

Contact Information for Business Card

We are open to designers suggestion and or design ideas.

Font styles to use
Serif
Sans Serif

Colors
3276b5
33a6d7
fffefd

Requirements
Must have
• Must have company logo , first and last name , phone number , web and email address, ect....

```html
<!DOCTYPE html>
<html lang="en">
<head>
<meta charset="utf-8">
<title>Vantrel Systems – Business Card</title>
<link href="https://fonts.googleapis.com/css2?family=Open+Sans:ital,wght@0,400;0,600;0,700;0,800;1,400;1,700&display=swap" rel="stylesheet">
<style>
  :root {
    --stage: #2b2b2d;
    --card: #161617;
    --brand-blue: #3276b5;
    --sky-blue: #33a6d7;
    --paper-white: #fffefd;
    --gloss: #3a3a3c;
  }
  * { box-sizing: border-box; margin: 0; padding: 0; }
  html, body {
    width: 1200px; height: 900px; overflow: hidden;
    background: var(--stage);
    font-family: "Open Sans", Arial, sans-serif;
    color: var(--paper-white);
  }
  .canvas {
    width: 1200px; height: 900px;
    display: flex; flex-direction: column;
    align-items: center; justify-content: center; gap: 36px;
  }
  .card {
    position: relative;
    width: 700px; height: 400px;
    background: var(--card);
    box-shadow: 0 14px 30px rgba(0,0,0,.45);
  }

  /* front */
  .front-brand {
    position: absolute; left: 56px; top: 150px;
    width: 320px;
    display: flex; align-items: center; gap: 10px;
    white-space: nowrap;
  }
  .brand-dot {
    width: 14px; height: 14px; border-radius: 50%;
    background: var(--brand-blue); flex: none;
  }
  .brand-name {
    font-weight: 800; font-size: 30px; letter-spacing: -0.3px;
    color: var(--brand-blue); line-height: 1;
  }
  .divider {
    position: absolute; left: 398px; top: 96px;
    width: 1px; height: 150px; background: var(--brand-blue);
  }
  .contact {
    position: absolute; left: 424px; top: 100px;
    white-space: nowrap;
  }
  .contact-name {
    font-weight: 700; font-style: italic; font-size: 22px;
    color: var(--brand-blue); text-transform: uppercase; letter-spacing: .3px;
  }
  .contact-title {
    font-style: italic; font-size: 16px; margin-bottom: 14px;
  }
  .contact-list { list-style: none; }
  .contact-list li {
    display: flex; align-items: center; gap: 10px;
    font-style: italic; font-size: 15px; line-height: 26px;
  }
  .contact-list svg { width: 13px; height: 13px; fill: var(--brand-blue); flex: none; }
  .address {
    position: absolute; left: 56px; bottom: 70px;
    font-style: italic; font-size: 15px;
  }

  /* back */
  .back-brand {
    position: absolute; left: 0; right: 0; top: 110px;
    display: flex; align-items: center; justify-content: center; gap: 16px;
    white-space: nowrap;
  }
  .back-brand .brand-dot { width: 26px; height: 26px; background: var(--gloss); }
  .back-brand .brand-name { font-size: 64px; color: var(--gloss); }
  .services {
    position: absolute; left: 0; right: 0; bottom: 70px;
    text-align: center; font-style: italic; font-size: 16px;
  }
  .services .sep { color: var(--sky-blue); margin: 0 8px; font-style: normal; }
</style>
</head>
<body>
<main class="canvas">
  <section class="card card-front" aria-label="Card front">
    <div class="front-brand">
      <span class="brand-dot"></span>
      <span class="brand-name">Vantrel Systems</span>
    </div>
    <div class="divider"></div>
    <div class="contact">
      <p class="contact-name">Dana Corwell</p>
      <p class="contact-title">President</p>
      <ul class="contact-list">
        <li>
          <svg viewBox="0 0 24 24" aria-hidden="true"><path d="M6.6 10.8a15.1 15.1 0 0 0 6.6 6.6l2.2-2.2a1 1 0 0 1 1-.25 11.4 11.4 0 0 0 3.6.57 1 1 0 0 1 1 1V20a1 1 0 0 1-1 1A17 17 0 0 1 3 4a1 1 0 0 1 1-1h3.5a1 1 0 0 1 1 1c0 1.25.2 2.45.57 3.57a1 1 0 0 1-.25 1z"/></svg>
          555.014.2270 ext 106
        </li>
        <li>
          <svg viewBox="0 0 24 24" aria-hidden="true"><path d="M2 5h20v14H2zm2 2v.5l8 5 8-5V7l-8 5z"/></svg>
          name@vantrelsecure.com
        </li>
        <li>
          <svg viewBox="0 0 24 24" aria-hidden="true"><path d="M12 2a10 10 0 1 0 0 20 10 10 0 0 0 0-20zm6.9 9h-3a15 15 0 0 0-1.3-5.5A8 8 0 0 1 18.9 11zM12 4c.9 1.2 1.8 3.7 1.9 7h-3.8C10.2 7.7 11.1 5.2 12 4zM9.4 5.5A15 15 0 0 0 8.1 11h-3a8 8 0 0 1 4.3-5.5zM5.1 13h3a15 15 0 0 0 1.3 5.5A8 8 0 0 1 5.1 13zM12 20c-.9-1.2-1.8-3.7-1.9-7h3.8c-.1 3.3-1 5.8-1.9 7zm2.6-1.5a15 15 0 0 0 1.3-5.5h3a8 8 0 0 1-4.3 5.5z"/></svg>
          www.vantrelsecure.com
        </li>
      </ul>
    </div>
    <p class="address">4210 Harbor Ln # 118, Lakeview Ohio 44000</p>
  </section>

  <section class="card card-back" aria-label="Card back">
    <div class="back-brand">
      <span class="brand-dot"></span>
      <span class="brand-name">Vantrel Systems</span>
    </div>
    <p class="services">
      Video Surveillance<span class="sep">•</span>Security Alarm<span class="sep">•</span>Fire Alarm<span class="sep">•</span>Access Control
    </p>
  </section>
</main>
</body>
</html>
```